We need a PowerPoint to outline what Modeling is about!

PowerPoint presentation to be shown to aspiring models. The students will be joining our 1-day workshop, and they will be taught the very basics of being a model.
What should be included in the slides:
• What is Modelling? - Description of Modelling, and what it takes to be a Model.
• Types of Models in the market - Catwalk Model / Photography Model / Events Model
• Expectations of a model - Professionalism, Punctuality, Confidence, etc etc.
• Practical (catwalk) tips: Posture
• Practical (catwalk) tips: How to do a simple catwalk
• Practical (photography) tips: How to bring out your best angles in photos
• Trainer Assessment of Students
Here are some definitions that we use. You may change the wording as you see fit, as long as the meaning is the same.
Modelling is to promote a product / brand / service in an advertisement, show, commercial or event.
Runway / Fashion Model – Walk the catwalk to promote clothing and accessories in a fashion show.
Most shows require the model to be tall and skinny. Model needs to strut with confidence and grace down the runway. Body shape more important than facial features.
Photography Model – Appear for Print Ads, Magazine Editorials, Posters, etc.
Height requirements are not as strict (or not present) as compared to Runway Model. Good features preferred, but not a must.
Video Model – Appear for TV commercials, Promotional Videos, etc.
Model needs to possess basic acting skills to promote the product, brand or service on video. Confidence and screen charisma more important than looks or body.
Events Model – Promote the product, brand or service during ‘live’ events and shows.
Model needs to be engaging and charismatic to ‘sell’ the product to customers.
A longer description can also be found here: http://www.brightlanecasting.sg/models/
Target Market(s)
Adults aged 18 - 40 who are interested to take up Modeling.
Industry/Entity Type
Events
Requirements
Must have
- Visually appealing! Does not have to be content heavy, but should deliver the message effectively.
Nice to have
- Pretty pictures.

```html
<!DOCTYPE html>
<html lang="en">
<head>
<meta charset="utf-8">
<title>Modelling Workshop – Slides</title>
<link rel="stylesheet" href="https://fonts.googleapis.com/css2?family=Open+Sans:wght@300;400;700&display=swap">
<style>
  :root {
    --board-dark: #1c1c1c;
    --board-mid: #2c2c2c;
    --slide-white: #ffffff;
    --band-dark: #333333;
    --band-text: #ffffff;
    --ink: #222222;
    --ink-soft: #333333;
    --photo-light: #eeeeee;
    --photo-mid: #c9c9c9;
    --photo-deep: #8a8a8a;
    --strip: #3a3a3a;
    --strip-text: #d8d8d8;
    --icon: #7a7a7a;
  }
  * { margin: 0; padding: 0; box-sizing: border-box; }
  html, body { width: 1200px; height: 1000px; overflow: hidden; }
  body {
    position: relative;
    font-family: "Open Sans", Verdana, sans-serif;
    color: var(--ink);
    background: linear-gradient(90deg, var(--board-dark), var(--board-mid) 50%, var(--board-dark));
  }
  .slide { position: absolute; background: var(--slide-white); overflow: hidden; }
  .slide-title {
    position: absolute; left: 0; top: 0;
    background: var(--band-dark); color: var(--band-text);
    font-weight: 400; letter-spacing: 0.5px; white-space: nowrap;
    display: flex; align-items: center;
  }
  .brand-box {
    position: absolute; background: var(--band-dark); color: var(--band-text);
    display: flex; flex-direction: column; justify-content: center;
    font-weight: 400; line-height: 1.15;
  }
  .photo { position: absolute; }

  /* Slide 1 – cover photo */
  .slide-cover { left: 6px; top: 38px; width: 577px; height: 434px; }
  .slide-cover .photo {
    inset: 0;
    background: linear-gradient(100deg, var(--photo-mid) 0%, var(--photo-light) 45%, #f6f6f6 70%, var(--photo-light) 100%);
  }
  .slide-cover .brand-box { right: 0; bottom: 0; width: 122px; height: 125px; padding-left: 13px; font-size: 23px; }

  /* Slide 2 – types */
  .slide-types { left: 600px; top: 38px; width: 578px; height: 434px; }
  .slide-types .slide-title { width: 572px; height: 59px; padding-left: 6px; font-size: 25.5px; }
  .model-type { position: absolute; left: 27px; top: 96px; width: 530px; font-size: 23px; line-height: 28px; color: var(--ink); }
  .model-type strong { font-weight: 700; }
  .model-note { position: absolute; left: 31px; top: 214px; width: 520px; font-size: 17px; line-height: 22px; color: var(--ink-soft); }
  .slide-types .brand-box { right: 0; bottom: 2px; width: 68px; height: 67px; padding-left: 6px; font-size: 12.5px; }

  /* Slide 3 – definition */
  .slide-definition { left: 16px; top: 541px; width: 579px; height: 431px; }
  .slide-definition .slide-title { width: 352px; height: 58px; padding-left: 16px; font-size: 26px; }
  .definition { position: absolute; left: 49px; top: 155px; width: 480px; font-size: 23px; line-height: 29px; color: var(--ink); }
  .definition strong { font-weight: 700; }
  .slide-definition .brand-box { right: 0; bottom: 0; width: 70px; height: 66px; padding-left: 6px; font-size: 12.5px; }

  /* Slide 4 – contact */
  .slide-contact { left: 613px; top: 548px; width: 563px; height: 422px; background: var(--photo-light); }
  .slide-contact .photo {
    inset: 0;
    background: linear-gradient(90deg, #f2f2f2 0%, var(--photo-mid) 15%, #f0f0f0 35%, var(--photo-mid) 50%, #f3f3f3 70%, var(--photo-mid) 85%, #f1f1f1 100%);
  }
  .slide-contact .slide-title { width: 188px; height: 55px; padding-left: 9px; font-size: 25px; }
  .contact-panel {
    position: absolute; left: 24px; top: 97px; width: 539px; height: 273px;
    background: rgba(255, 255, 255, 0.8);
    font-size: 13.5px; line-height: 17px; color: var(--ink);
  }
  .contact-heading { position: absolute; font-size: 20px; font-weight: 700; }
  .find-us { left: 19px; top: 6px; }
  .call-us { left: 264px; top: 2px; }
  .address { position: absolute; left: 14px; top: 39px; }
  .phones { position: absolute; left: 261px; top: 35px; }
  .team { position: absolute; left: 19px; top: 94px; }
  .team h3 { font-size: 14px; font-weight: 700; }
  .social-strip {
    position: absolute; left: 0; top: 370px; width: 445px; height: 52px;
    background: var(--strip); display: flex; align-items: center; padding-left: 62px; gap: 22px;
  }
  .social-link { display: flex; align-items: center; gap: 8px; color: var(--strip-text); font-size: 10px; line-height: 11px; }
  .social-dot { width: 34px; height: 34px; border-radius: 50%; background: var(--icon); flex: none; }
  .slide-contact .brand-box { right: 0; bottom: 0; width: 118px; height: 120px; padding-left: 11px; font-size: 20px; }
</style>
</head>
<body>

  <section class="slide slide-cover">
    <div class="photo" role="img" aria-label="Fashion photo of a young man and woman posing beside white columns"></div>
    <div class="brand-box">BRIGHT<br>LANE<br>CASTING</div>
  </section>

  <section class="slide slide-types">
    <h2 class="slide-title">TYPES OF THE MODELS IN THE MARKET</h2>
    <p class="model-type"><strong>Runway / Fashion Model</strong> – Walk the catwalk to promote clothing and accessories in a fashion show.</p>
    <p class="model-note">Most shows require the model to be tall and skinny. Model needs to strut with confidence and grace down the runway. Body shape more important than facial features.</p>
    <div class="brand-box">BRIGHT<br>LANE<br>CASTING</div>
  </section>

  <section class="slide slide-definition">
    <h2 class="slide-title">WHAT IS MODELLING?</h2>
    <p class="definition"><strong>Modelling</strong> is to promote a product / brand / service in an advertisement, show, commercial or event.</p>
    <div class="brand-box">BRIGHT<br>LANE<br>CASTING</div>
  </section>

  <section class="slide slide-contact">
    <div class="photo" role="img" aria-label="Faded black and white photo of three models posing in dresses"></div>
    <h2 class="slide-title">THANK YOU</h2>
    <div class="contact-panel">
      <h3 class="contact-heading find-us">Find Us!</h3>
      <p class="address">42 Harbour Lane #03-11<br>Singapore 418802</p>
      <h3 class="contact-heading call-us">Call Us!</h3>
      <p class="phones">Tel: +65 6210 4385 (Office Hours)<br>Mobile:+65 9182 7730 (After Hours)<br>Fax: +65 6210 4390</p>
      <div class="team">
        <h3>THE TEAM at BRIGHT LANE</h3>
        <p>For general enquiries,<br>contact@brightlanecasting.sg<br>For bookings,<br>mei@brightlanecasting.sg<br>For talent and recruitment matters,<br>anna@brightlanecasting.sg<br>For marketing, media and account matters,<br>leon@brightlanecasting.sg</p>
      </div>
    </div>
    <nav class="social-strip">
      <span class="social-link"><span class="social-dot"></span>Like Us on<br>Pinwall</span>
      <span class="social-link"><span class="social-dot"></span>Follow Us on<br>Chirper</span>
      <span class="social-link"><span class="social-dot"></span>Subscribe on<br>ClipTube</span>
    </nav>
    <div class="brand-box">BRIGHT<br>LANE<br>CASTING</div>
  </section>

</body>
</html>
```